R & T Summit Construction Business Card ideas

We want a business card to represents our company in a way that looks professional but is also a business card that is unique!

Industry/Entity Type

Construction Company

Contact Information for Business Card

open to all design ideas, just want to be able to see different options to choose from in either color or grayscale.

Requirements
Must have
• Our names and phone numbers
• Corwin Tallage 404-555-0142
• Derek Walsh 386-555-0187
• Business logo

```html
<!DOCTYPE html>
<html lang="en">
<head>
<meta charset="utf-8">
<meta name="format-detection" content="telephone=no,email=no,address=no">
<title>R &amp; T Summit Construction – Business Card</title>
<link rel="stylesheet" href="https://fonts.googleapis.com/css2?family=Cinzel:wght@500&family=Montserrat:wght@300;400;700&display=swap">
<style>
  :root {
    --page: #e4e1dc;
    --ink: #111111;
    --paper: #f4f4f4;
    --silver: #a9a9a9;
    --text-light: #ffffff;
    --text-muted: #d6d6d6;
  }
  * { box-sizing: border-box; margin: 0; padding: 0; }
  html, body { width: 1200px; height: 1023px; overflow: hidden; }
  body {
    background: var(--page);
    font-family: "Montserrat", sans-serif;
    position: relative;
  }
  .card {
    position: absolute;
    left: 240px;
    width: 720px;
    height: 412px;
    border-radius: 28px;
    overflow: hidden;
    box-shadow: 0 10px 28px rgba(0,0,0,0.25);
  }
  .card--contact { top: 66px; }
  .card--front { top: 545px; }
  .card__shape { position: absolute; inset: 0; width: 100%; height: 100%; }

  .brand {
    position: absolute;
    display: flex;
    align-items: center;
    gap: 14px;
    font-family: "Cinzel", serif;
    font-weight: 500;
    color: var(--ink);
    line-height: 1.15;
  }
  .brand__mark {
    width: 16px; height: 16px;
    background: var(--ink);
    flex: none;
  }
  .brand__name { font-size: 26px; letter-spacing: 0.5px; }
  .card--contact .brand { left: 34px; top: 176px; }
  .card--contact .brand__name { font-size: 22px; }
  .card--front .brand { left: 230px; top: 172px; }
  .card--front .brand__name { font-size: 30px; }

  .contact {
    position: absolute;
    left: 430px;
    top: 74px;
    color: var(--text-light);
  }
  .contact__name {
    font-weight: 700;
    font-size: 20px;
    letter-spacing: 0.5px;
  }
  .contact__role {
    font-weight: 300;
    font-size: 15px;
    color: var(--text-muted);
    margin-top: 2px;
  }
  .contact__list { list-style: none; margin-top: 26px; }
  .contact__item {
    display: flex;
    align-items: center;
    gap: 10px;
    font-weight: 300;
    font-size: 15px;
    color: var(--text-light);
    margin-bottom: 6px;
  }
  .contact__icon { width: 13px; height: 13px; flex: none; }
  .contact__address {
    font-weight: 300;
    font-size: 15px;
    line-height: 1.4;
    color: var(--text-light);
    margin-top: 24px;
  }
</style>
</head>
<body>

  <section class="card card--contact" aria-label="Business card, contact side">
    <svg class="card__shape" viewBox="0 0 720 412" preserveAspectRatio="none" aria-hidden="true">
      <rect width="720" height="412" fill="var(--ink)"/>
      <path d="M0 0 H322 C402 120 402 292 322 412 H0 Z" fill="var(--silver)"/>
      <path d="M0 0 H306 C386 120 386 292 306 412 H0 Z" fill="var(--ink)"/>
      <path d="M0 0 H296 C374 120 374 292 296 412 H0 Z" fill="var(--paper)"/>
    </svg>

    <div class="brand">
      <span class="brand__mark"></span>
      <span class="brand__name">R &amp; T Summit<br>Construction</span>
    </div>

    <div class="contact">
      <p class="contact__name">CORWIN TALLAGE</p>
      <p class="contact__role">Managing Director</p>
      <ul class="contact__list">
        <li class="contact__item">
          <svg class="contact__icon" viewBox="0 0 16 16" aria-hidden="true"><path d="M3.5 1 L6 1 L7 5 L5.3 6.3 C6.2 8.2 7.8 9.8 9.7 10.7 L11 9 L15 10 L15 12.5 C15 13.9 13.9 15 12.5 15 C6.7 15 1 9.3 1 3.5 C1 2.1 2.1 1 3.5 1 Z" fill="#fff"/></svg>
          <span>404-555-0142</span>
        </li>
        <li class="contact__item">
          <svg class="contact__icon" viewBox="0 0 16 16" aria-hidden="true"><rect x="1" y="3" width="14" height="10" fill="#fff"/><path d="M1 3 L8 9 L15 3" fill="none" stroke="var(--ink)" stroke-width="1.4"/></svg>
          <span>info@rtsummit.com</span>
        </li>
        <li class="contact__item">
          <svg class="contact__icon" viewBox="0 0 16 16" aria-hidden="true"><circle cx="8" cy="8" r="7" fill="#fff"/><path d="M1 8 H15 M8 1 C4 5 4 11 8 15 M8 1 C12 5 12 11 8 15" fill="none" stroke="var(--ink)" stroke-width="1"/></svg>
          <span>www.rtsummit.com</span>
        </li>
      </ul>
      <p class="contact__address">Here your company<br>or home address</p>
    </div>
  </section>

  <section class="card card--front" aria-label="Business card, logo side">
    <svg class="card__shape" viewBox="0 0 720 412" preserveAspectRatio="none" aria-hidden="true">
      <rect width="720" height="412" fill="var(--paper)"/>
      <path d="M0 0 H150 C70 130 80 300 190 412 H0 Z" fill="var(--silver)"/>
      <path d="M0 0 H136 C56 130 66 300 174 412 H0 Z" fill="var(--paper)"/>
      <path d="M0 0 H126 C46 130 56 300 162 412 H0 Z" fill="var(--ink)"/>
    </svg>

    <div class="brand">
      <span class="brand__mark"></span>
      <span class="brand__name">R &amp; T Summit<br>Construction</span>
    </div>
  </section>

</body>
</html>
```